Creative Web Designer: Refresh & Elevate our Beach Lifestyle Brand with a Joyful, Elegant Red...

Thalori (thalori.gr), a vibrant Greek brand celebrated for its high-quality beachwear and accessories, is embarking on an exciting phase as we enter our third year. Renowned for our stylish flip flops, beach towels, and caps, we are thrilled to announce the expansion of our product line with innovative beach essentials and a fresh palette for our existing collection.
As we continue to grow and evolve, we are in search of a talented and imaginative web designer who can capture the essence of Thalori and translate it into a digital experience. Our ideal candidate will craft a website that mirrors the happiness and relaxation of a day at the beach, while also embodying the sophistication and elegance that our brand represents.
Your Mission:
Design a Website That Reflects Our Brand Identity: Create a website that is visually stunning, easy to navigate, and showcases our products in a way that feels both refreshing and luxurious.
Incorporate New Product Lines and Colors: Seamlessly integrate our new beach products and color schemes, ensuring the website remains cohesive and on-brand.
User Experience is Key: Design a user-friendly interface that ensures a seamless shopping experience for our customers, with intuitive navigation and a mobile-responsive design.
Embrace Creativity While Staying Elegant: We want our website to be a reflection of the joy and elegance that our products bring to our customers. Your design should be innovative, incorporating modern web design trends that align with our brand's aesthetic.
What We're Looking For:
A portfolio that demonstrates experience in creating visually appealing and user-friendly e-commerce websites.
Strong understanding of branding and the ability to translate a brand's essence into a digital format.
Proficiency in the latest web design software and technologies.
Excellent communication skills and the ability to work collaboratively with our team to bring our vision to life.
This is a fantastic opportunity for a web designer who loves the beach lifestyle and is passionate about creating beautiful, effective websites. If you're ready to dive into a project that will challenge and excite you, while making a significant impact on our growing brand, we would love to hear from you.
Regarding the products, on the website (thalori.gr) you will the flips flops and on the attached powerpoint all the accessories for this summer. Please use the images to craft your designs.
Join us in making Thalori the go-to brand for beach enthusiasts everywhere. Apply now to start the conversation and share your vision for our new website 😊🩴☀️⛱️
p.s. we didn;t mention the pages to be designed. Its 4 pages in all,
homepage, product category page, singleproduct page and contact us page
Number of Pages Required
4 page
Look and feel
Each slider illustrates characteristics of the customer's brand and the style your logo design should communicate.

```html
<!DOCTYPE html>
<html lang="en">
<head>
<meta charset="utf-8">
<title>Thalori – Summerwear Landing Page</title>
<link href="https://fonts.googleapis.com/css2?family=Bebas+Neue&family=Inria+Sans:wght@300;400;700&display=swap" rel="stylesheet">
<style>
:root{
  --navy:#281F65;
  --mist:#E9E9F0;
  --sun:#FFFF56;
  --card:#ECECF3;
  --ink:#1d1a33;
  --white:#ffffff;
  --display:'Bebas Neue', sans-serif;
  --body:'Inria Sans', sans-serif;
}
*{margin:0;padding:0;box-sizing:border-box}
html,body{width:761px;height:1200px;overflow:hidden;background:var(--mist)}
.board{position:relative;width:761px;height:1200px;overflow:hidden;background:var(--mist);font-family:var(--body);color:var(--ink)}
.abs{position:absolute}
.backdrop{position:absolute;left:0;top:0}
.board-title{position:absolute;left:0;width:761px;top:42px;text-align:center;font-family:var(--display);font-weight:400;font-size:50px;line-height:1;color:#0d0d12;letter-spacing:.3px}
.board-title span{color:var(--navy)}

.spec{position:absolute;right:48px;width:240px;text-align:right;color:var(--white)}
.spec-head{top:254px;font-family:var(--display);font-size:36px;line-height:1}
.spec-bebas{top:299px;font-family:var(--display);font-size:20px;line-height:1}
.spec-bebas-text{top:327px;font-family:var(--display);font-size:7.6px;line-height:11px}
.spec-inria{top:376px;font-family:var(--body);font-weight:300;font-size:18px;line-height:1;letter-spacing:.5px}
.spec-inria-text{top:403px;font-family:var(--body);font-weight:300;font-size:6.3px;line-height:8px}
.swatch{position:absolute;top:473px;width:77px;height:77px;display:flex;align-items:center;justify-content:center;font-family:var(--display);font-size:11px}
.swatch-navy{left:473.5px;background:var(--navy);border:1px solid var(--white);color:var(--white)}
.swatch-mist{left:555px;background:var(--mist);color:var(--navy)}
.swatch-sun{left:636.5px;background:var(--sun);color:var(--navy)}

.watermark{position:absolute;right:51px;font-family:var(--display);font-size:162px;line-height:1;color:rgba(40,31,101,.11);text-align:right;pointer-events:none}
.wm-1{top:752px}
.wm-2{top:885px}

.page{position:absolute;left:49px;top:116px;width:410px;height:1045.5px;background:var(--white);box-shadow:0 2px 10px rgba(40,31,101,.12);overflow:hidden}
.topbar{position:absolute;left:0;top:0;width:410px;height:10.5px;background:var(--navy);color:var(--white);font-size:3.4px;display:flex;align-items:center;justify-content:space-between;padding:0 51px}
.topbar .dot{display:inline-block;width:4px;height:4px;border-radius:50%;background:var(--sun);vertical-align:middle;margin:0 3px}
.menu-btn{left:51.5px;top:18.5px;width:13.5px;height:10px;background:var(--navy);border-radius:1.5px}
.menu-btn i{position:absolute;left:3px;height:.6px;background:var(--white)}
.brand{left:0;width:410px;top:14px;text-align:center;color:var(--navy)}
.brand-name{font-family:var(--body);font-weight:400;font-size:15px;line-height:1}
.brand-sub{font-size:3.4px;letter-spacing:.8px;margin-top:1px}
.cart{left:317px;top:19px}
.pill{position:absolute;display:flex;align-items:center;justify-content:center;gap:3px;border-radius:10px;font-weight:700}
.pill-outline{background:var(--white);border:.7px solid var(--navy);color:var(--navy)}
.pill-navy{background:var(--navy);color:var(--white)}
.pill-light{background:var(--white);color:var(--navy)}
.pill svg{display:block}
.signup{left:331px;top:18.5px;width:27.5px;height:10.5px;font-size:3.4px}

.hero{left:51.5px;top:36.5px;width:307px;height:49px;border:.8px solid var(--navy);border-radius:5px;background:#f6f6f9;text-align:center}
.hero-title{margin-top:9px;font-family:var(--display);font-weight:400;font-size:16px;line-height:1;color:var(--navy)}
.hero-text{width:230px;margin:3px auto 0;font-size:3.4px;line-height:4.5px;color:var(--ink)}
.hero-shop{left:184.5px;top:81px;width:40.5px;height:9.5px;font-size:3.4px}

.slide{position:absolute;top:106.5px;width:54px;height:86px;border-radius:4px;overflow:hidden}
.slide-label{position:absolute;left:5px;bottom:10px;font-family:var(--display);font-size:6.3px;color:var(--white);line-height:1}
.slide-main{left:171.5px;top:100px;width:66.5px;height:99px;border-radius:5px;display:flex;align-items:center;justify-content:center}
.slide-main span{font-family:var(--display);font-size:15px;color:var(--white);line-height:1}
.seeall-center{left:184.5px;top:194px;width:41px;height:9px;font-size:3.4px}
.arrow-btn{position:absolute;top:148px;width:8px;height:8px;border-radius:50%;background:var(--navy);display:flex;align-items:center;justify-content:center}

.values{left:0;top:213px;width:410px;height:51px;background:linear-gradient(180deg,#a9c6e2 0%,#d4e3f0 55%,#bcd3e8 100%)}
.value{position:absolute;top:9.5px;width:90px}
.value h3{font-family:var(--display);font-weight:400;font-size:6.4px;color:var(--navy);line-height:1}
.value p{margin-top:3.5px;font-size:3.5px;line-height:4.6px;color:#2c2a44}

.section-title{position:absolute;left:51.5px;font-family:var(--display);font-weight:400;font-size:11.5px;line-height:1;color:var(--navy)}
.seeall{left:318.5px;width:40px;height:9.5px;font-size:3.4px}

.pcard{position:absolute;background:var(--card);border-radius:3px;overflow:hidden}
.pimg{position:relative;width:100%}
.heart{position:absolute;top:3px;right:3px;width:5px;height:5px;border-radius:50%;background:var(--navy)}
.pinfo{padding:2.3px 3px 0}
.prow{display:flex;justify-content:space-between;font-size:3.5px;font-weight:700;color:var(--ink);line-height:1.2}
.psub{font-size:2.1px;color:#444;margin-top:1px}
.stars{font-size:2.6px;color:#f2b705;margin-top:.6px}
.stars b{color:#555;font-weight:400;margin-left:1px}
.padd{display:inline-block;margin-top:1.4px;border:.5px solid var(--navy);border-radius:5px;font-size:2px;font-weight:700;color:var(--navy);padding:.5px 3px}
.pcard-big .pinfo{padding:6px 8px 0}
.pcard-big .prow{font-size:6.4px;font-weight:400}
.pcard-big .psub{font-size:3.5px;margin-top:2.5px}
.pcard-big .stars{font-size:4.6px;margin-top:1.5px}
.pcard-big .padd{font-size:3.4px;padding:1.3px 5px;margin-top:3px;border-width:.7px}
.pcard-big .heart{width:10px;height:10px;top:5px;right:5px}

.promo{left:0;top:428px;width:410px;height:127px;background:var(--navy)}
.promo-title{position:absolute;left:51.5px;top:26px;font-family:var(--display);font-weight:400;font-size:12.5px;line-height:1;color:var(--white)}
.promo-title span{color:var(--sun)}
.promo-text{position:absolute;left:51.5px;top:42px;width:127px;font-size:3.5px;line-height:4.7px;color:#e6e5f2}
.promo-shop{left:51.5px;top:502.5px;width:40px;height:9px;font-size:3.4px}
.promo-img{position:absolute;border-radius:4px}

.cat{position:absolute;top:527.5px;width:99px;height:66.5px;border-radius:4px;background:linear-gradient(160deg,#f7f7f9,#e6e6ec);box-shadow:0 2px 5px rgba(40,31,101,.12);overflow:hidden}
.cat-img{position:absolute;right:0;top:0;width:62px;height:36px}
.cat-label{position:absolute;left:4px;top:48px;font-family:var(--display);font-size:6.2px;line-height:1;color:var(--navy)}
.cat-shop{position:absolute;right:4.5px;top:59px;width:38px;height:9px;font-size:3.2px}

.svc{position:absolute;top:809px;width:98px;height:98.5px;background:var(--card);border-radius:3px;overflow:hidden}
.svc-img{width:100%;height:64.5px}
.svc h4{margin:6px 0 0 4px;font-size:5.4px;font-weight:700;line-height:1;color:var(--ink)}
.svc p{margin:2px 0 0 4px;font-size:3.2px;color:#444}
.svc .padd{margin:3.5px 0 0 4px;font-size:3px;padding:1px 4px}

.footer{left:0;top:918.5px;width:410px;height:127px;background:var(--navy);color:var(--white)}
.foot-links{position:absolute;left:51.5px;top:12px;font-size:3.5px;display:flex;gap:7px}
.foot-follow{position:absolute;right:51.5px;top:10.5px;display:flex;align-items:center;gap:6px;font-size:3.5px}
.foot-follow i{display:block;width:4.5px;height:4.5px;border-radius:50%;background:var(--white)}
.foot-rule{position:absolute;left:51.5px;width:307px;height:.5px;background:rgba(255,255,255,.55)}
.foot-col{position:absolute;top:33px}
.foot-col h5{font-family:var(--display);font-weight:400;font-size:4.6px;line-height:1;margin-bottom:5px}
.foot-col li{list-style:none;font-size:3.5px;line-height:9.4px}
.sub-box{position:absolute;left:284px;top:41.5px;width:74.5px;height:7px;background:var(--white);border-radius:1px}
.sub-box span{position:absolute;right:.8px;top:.8px;height:5.4px;width:15px;background:var(--navy);color:var(--white);font-size:3px;display:flex;align-items:center;justify-content:center}
.apps{position:absolute;left:284px;top:59px}
.apps h5{font-family:var(--display);font-weight:400;font-size:4.6px;line-height:1;margin-bottom:4px}
.apps li{list-style:none;font-size:3.5px;line-height:9.4px;display:flex;align-items:center;gap:3px}
.apps li i{display:block;width:3.5px;height:3.5px;border-radius:50%;background:var(--white)}
.copyright{position:absolute;left:51.5px;top:112px;font-size:3.4px}
</style>
</head>
<body>
<div class="board">
  <svg class="backdrop" width="761" height="1200" aria-hidden="true">
    <polygon points="0,544 761,122 761,610 0,610" fill="#281F65"/>
  </svg>

  <h1 class="board-title">Thalori - <span>Sumerwear</span></h1>

  <div class="spec spec-head">Typography</div>
  <div class="spec spec-bebas">Bebas Neue</div>
  <p class="spec spec-bebas-text">It is a long established fact that a reader will be distracted by the readable content of a page when looking at its layout. The point of using Lorem Ipsum is that it has a more-or-less normal distribution of letters, as opposed to using 'Content here, content here',</p>
  <div class="spec spec-inria">INRIA SANS</div>
  <p class="spec spec-inria-text">It Is A Long Established Fact That A Reader Will Be Distracted By The Readable Content Of A Page When Looking At Its Layout. The Point Of Using Lorem Ipsum Is That It Has A More-Or-Less Normal Distribution Of Letters, As Opposed To Using 'Content Here, Content Here',</p>

  <div class="swatch swatch-navy">#281F65</div>
  <div class="swatch swatch-mist">#E9E9F0</div>
  <div class="swatch swatch-sun">#FFFF56</div>

  <main class="page">
    <div class="topbar">
      <span><i class="dot"></i>+30 210 555 0142 | +30 690 555 0178</span>
      <span>info@thalori.gr<i class="dot"></i></span>
    </div>

    <div class="abs menu-btn"><i style="top:3px;width:7px"></i><i style="top:5px;width:5px"></i><i style="top:7px;width:6px"></i></div>
    <div class="abs brand"><div class="brand-name">Thalori</div><div class="brand-sub">SUMMERWEAR</div></div>
    <svg class="abs cart" width="9" height="9" viewBox="0 0 9 9" aria-label="Cart">
      <path d="M.5 1.5h1.4l1.2 4.5h4.2l1-3.2H2.4" fill="none" stroke="#281F65" stroke-width=".7"/>
      <circle cx="3.6" cy="7.6" r=".7" fill="#281F65"/><circle cx="6.8" cy="7.6" r=".7" fill="#281F65"/>
      <circle cx="7.3" cy="1.3" r="1.3" fill="#FFFF56"/>
    </svg>
    <div class="pill pill-outline signup">Sign Up</div>

    <section class="abs hero">
      <h2 class="hero-title">Thalori - Summerwear</h2>
      <p class="hero-text">It is a long established fact that a reader will be distracted by the readable content of a page when looking at its layout. The point of using Lorem Ipsum is that it has a more-or-less normal distribution of letters, as opposed to using 'Content here, content here', making it look like readable English. Many desktop publishing packages and web page editors now use</p>
    </section>
    <div class="pill pill-outline hero-shop">Shop <svg width="11" height="3"><path d="M0 1.5h10M8.5.3 10 1.5 8.5 2.7" stroke="#281F65" stroke-width=".5" fill="none"/></svg></div>

    <div class="slide" style="left:55px;background:linear-gradient(160deg,#9a9ca4,#4f5058)" role="img" aria-label="Patterned jungle hat with chin cord"><span class="slide-label">Jungle Hats</span></div>
    <div class="slide" style="left:113.5px;background:linear-gradient(160deg,#c7c9cf,#7a7e96)" role="img" aria-label="Colourful patterned jokey cap"><span class="slide-label">Jokey Caps</span></div>
    <div class="slide slide-main" style="background:linear-gradient(170deg,#8e5d8a,#6f4a79)" role="img" aria-label="Blue drawstring beach bag"><span>Beach Bag</span></div>
    <div class="slide" style="left:242.5px;background:linear-gradient(160deg,#e1e0e3,#c98a9a)" role="img" aria-label="Pink and red patterned pouches"><span class="slide-label">Pouches</span></div>
    <div class="slide" style="left:300.5px;background:linear-gradient(160deg,#9fb1b8,#61707a)" role="img" aria-label="Patterned bucket hat"><span class="slide-label">Buckets</span></div>
    <div class="pill pill-navy seeall-center">See All <svg width="11" height="3"><path d="M0 1.5h10M8.5.3 10 1.5 8.5 2.7" stroke="#fff" stroke-width=".5" fill="none"/></svg></div>
    <div class="arrow-btn" style="left:51.5px"><svg width="5" height="3"><path d="M5 1.5H.5M1.7.3.5 1.5l1.2 1.2" stroke="#fff" stroke-width=".5" fill="none"/></svg></div>
    <div class="arrow-btn" style="left:350.5px"><svg width="5" height="3"><path d="M0 1.5h4.5M3.3.3 4.5 1.5 3.3 2.7" stroke="#fff" stroke-width=".5" fill="none"/></svg></div>

    <section class="abs values" role="img" aria-label="Soft cloudy blue sky">
      <div class="value" style="left:55.5px"><h3>Designed in Greece</h3><p>Thalori has Greek DNA. Our designs are exclusively inspired by what makes Greece so unique - its summer. Our mission is to give you a taste by wearing our flip flops.</p></div>
      <div class="value" style="left:159.5px"><h3>Sustainability</h3><p>We care deeply about the environment in which we live and want to contribute to a more sustainable future through our efforts. Therefore, Thalori flip flops are produced from 100% recyclable, natural rubber.</p></div>
      <div class="value" style="left:263.5px"><h3>Comfort &amp; Style</h3><p>Our flip flops are designed to offer you a unique sense of comfort throughout your summer experiences. Wear them to the beach, on a walk or just for a coffee or a drink with your friends</p></div>
    </section>

    <h2 class="section-title" style="top:276px">Featured Products</h2>
    <div class="pill pill-navy seeall" style="top:277px">See All <svg width="11" height="3"><path d="M0 1.5h10M8.5.3 10 1.5 8.5 2.7" stroke="#fff" stroke-width=".5" fill="none"/></svg></div>

    <article class="pcard pcard-big" style="left:51.5px;top:295px;width:119.5px;height:122px">
      <div class="pimg" style="height:79px;background:linear-gradient(150deg,#f1efe8,#f2c7a5)" role="img" aria-label="Printed pouch with crab and coral design"><i class="heart"></i></div>
      <div class="pinfo"><div class="prow"><span>Pouch - Lorem Ipsum</span><span>€ 16.90</span></div><div class="psub">6 Different Designs Available</div><div class="stars">★★★★★<b>(12)</b></div><span class="padd">Add to cart</span></div>
    </article>

    <article class="pcard" style="left:177.5px;top:295px;width:56px;height:58px"><div class="pimg" style="height:36.5px;background:linear-gradient(160deg,#e8c6cc,#f0d9b4)" role="img" aria-label="Striped tote bag"><i class="heart"></i></div><div class="pinfo"><div class="prow"><span>Bag - Lorem Ipsum</span><span>€ 16.90</span></div><div class="psub">6 Different Designs Available</div><div class="stars">★★★★★<b>(12)</b></div><span class="padd">Add to cart</span></div></article>
    <article class="pcard" style="left:240px;top:295px;width:56px;height:58px"><div class="pimg" style="height:36.5px;background:linear-gradient(160deg,#a8c3cc,#c7a98a)" role="img" aria-label="Patterned bucket hat"><i class="heart"></i></div><div class="pinfo"><div class="prow"><span>Pouch - Lorem Ipsum</span><span>€ 16.90</span></div><div class="psub">6 Different Designs Available</div><div class="stars">★★★★★<b>(12)</b></div><span class="padd">Add to cart</span></div></article>
    <article class="pcard" style="left:302.5px;top:295px;width:56px;height:58px"><div class="pimg" style="height:36.5px;background:linear-gradient(160deg,#d9d9dd,#55545e)" role="img" aria-label="Dark patterned cap"><i class="heart"></i></div><div class="pinfo"><div class="prow"><span>Pouch - Lorem Ipsum</span><span>€ 16.90</span></div><div class="psub">6 Different Designs Available</div><div class="stars">★★★★★<b>(12)</b></div><span class="padd">Add to cart</span></div></article>
    <article class="pcard" style="left:177.5px;top:359.5px;width:56px;height:57.5px"><div class="pimg" style="height:36.5px;background:linear-gradient(160deg,#f1b7b3,#e95a5a)" role="img" aria-label="Colourful scrunchie"><i class="heart"></i></div><div class="pinfo"><div class="prow"><span>Pouch - Lorem Ipsum</span><span>€ 16.90</span></div><div class="psub">6 Different Designs Available</div><div class="stars">★★★★★<b>(12)</b></div><span class="padd">Add to cart</span></div></article>
    <article class="pcard" style="left:240px;top:359.5px;width:56px;height:57.5px"><div class="pimg" style="height:36.5px;background:linear-gradient(160deg,#cfcfd3,#35323f)" role="img" aria-label="Dark patterned tote bag"><i class="heart"></i></div><div class="pinfo"><div class="prow"><span>Pouch - Lorem Ipsum</span><span>€ 16.90</span></div><div class="psub">6 Different Designs Available</div><div class="stars">★★★★★<b>(12)</b></div><span class="padd">Add to cart</span></div></article>
    <article class="pcard" style="left:302.5px;top:359.5px;width:56px;height:57.5px"><div class="pimg" style="height:36.5px;background:linear-gradient(160deg,#8fd1c6,#c9a7d8)" role="img" aria-label="Striped beach towel"><i class="heart"></i></div><div class="pinfo"><div class="prow"><span>Pouch - Lorem Ipsum</span><span>€ 16.90</span></div><div class="psub">6 Different Designs Available</div><div class="stars">★★★★★<b>(12)</b></div><span class="padd">Add to cart</span></div></article>

    <section class="abs promo">
      <h2 class="promo-title">Umbrella &amp; <span>Beach Bag</span></h2>
      <p class="promo-text">It is a long established fact that a reader will be distracted by the readable content of a page when looking at its layout. The point of using Lorem Ipsum is that it has a more-or-less normal distribution of letters, as opposed to using 'Content here, content here', making it look like readable English. Many desktop publishing packages and web page editors now use</p>
      <div class="promo-img" style="left:231.5px;top:19.5px;width:97.5px;height:69.5px;background:linear-gradient(160deg,#6f92d6,#f0c98c 55%,#5b82cf)" role="img" aria-label="Patterned beach umbrella on blue background"></div>
      <div class="promo-img" style="left:210.5px;top:29.5px;width:35px;height:49px;background:linear-gradient(160deg,#e6937f,#3f8c92)" role="img" aria-label="Teal drawstring bag on coral background"></div>
      <div class="promo-img" style="left:320.5px;top:10px;width:38px;height:49px;background:linear-gradient(160deg,#e57e6f,#f1d4c8)" role="img" aria-label="Patterned pouch on coral background"></div>
    </section>
    <div class="pill pill-light promo-shop">Shop Now <svg width="11" height="3"><path d="M0 1.5h10M8.5.3 10 1.5 8.5 2.7" stroke="#281F65" stroke-width=".5" fill="none"/></svg></div>

    <div class="cat" style="left:51.5px"><div class="cat-img" style="background:linear-gradient(160deg,#e85d75,#f2d9d9)" role="img" aria-label="Pink patterned pouch"></div><span class="cat-label">Pouches - Thalori</span><div class="pill pill-outline cat-shop">Shop Now <svg width="10" height="3"><path d="M0 1.5h9M7.5.3 9 1.5 7.5 2.7" stroke="#281F65" stroke-width=".5" fill="none"/></svg></div></div>
    <div class="cat" style="left:155.5px"><div class="cat-img" style="background:linear-gradient(160deg,#f08a5d,#f2e6dc)" role="img" aria-label="Orange striped towel"></div><span class="cat-label">Towel - Thalori</span><div class="pill pill-outline cat-shop">Shop Now <svg width="10" height="3"><path d="M0 1.5h9M7.5.3 9 1.5 7.5 2.7" stroke="#281F65" stroke-width=".5" fill="none"/></svg></div></div>
    <div class="cat" style="left:259.5px"><div class="cat-img" style="background:linear-gradient(160deg,#c89b7b,#9fb6b4)" role="img" aria-label="Patterned bucket hat"></div><span class="cat-label">Buckets - Thalori</span><div class="pill pill-outline cat-shop">Shop Now <svg width="10" height="3"><path d="M0 1.5h9M7.5.3 9 1.5 7.5 2.7" stroke="#281F65" stroke-width=".5" fill="none"/></svg></div></div>

    <h2 class="section-title" style="top:608px">Most Selling Products</h2>
    <div class="pill pill-navy seeall" style="top:609.5px">See All <svg width="11" height="3"><path d="M0 1.5h10M8.5.3 10 1.5 8.5 2.7" stroke="#fff" stroke-width=".5" fill="none"/></svg></div>

    <article class="pcard" style="left:51.5px;top:625.5px;width:72.5px;height:73.5px"><div class="pimg" style="height:47.5px;background:linear-gradient(160deg,#e8c6cc,#f0d9b4)" role="img" aria-label="Striped tote bag"><i class="heart"></i></div><div class="pinfo"><div class="prow"><span>Bag - Lorem Ipsum</span><span>€ 16.90</span></div><div class="psub">6 Different Designs Available</div><div class="stars">★★★★★<b>(12)</b></div><span class="padd">Add to cart</span></div></article>
    <article class="pcard" style="left:129.5px;top:625.5px;width:72.5px;height:73.5px"><div class="pimg" style="height:47.5px;background:linear-gradient(160deg,#a8c3cc,#c7a98a)" role="img" aria-label="Patterned bucket hat"><i class="heart"></i></div><div class="pinfo"><div class="prow"><span>Bucket - Lorem Ipsum</span><span>€ 16.90</span></div><div class="psub">6 Different Designs Available</div><div class="stars">★★★★★<b>(12)</b></div><span class="padd">Add to cart</span></div></article>
    <article class="pcard" style="left:207.5px;top:625.5px;width:72.5px;height:73.5px"><div class="pimg" style="height:47.5px;background:linear-gradient(160deg,#e2e2e6,#4f4e59)" role="img" aria-label="Dark patterned cap"><i class="heart"></i></div><div class="pinfo"><div class="prow"><span>Jokey - Cap</span><span>€ 16.90</span></div><div class="psub">6 Different Designs Available</div><div class="stars">★★★★★<b>(12)</b></div><span class="padd">Add to cart</span></div></article>
    <article class="pcard" style="left:286px;top:625.5px;width:72.5px;height:73.5px"><div class="pimg" style="height:47.5px;background:linear-gradient(160deg,#f3efe4,#e9c69a)" role="img" aria-label="Printed cream pouch"><i class="heart"></i></div><div class="pinfo"><div class="prow"><span>Pouch - Lorem Ipsum</span><span>€ 16.90</span></div><div class="psub">6 Different Designs Available</div><div class="stars">★★★★★<b>(12)</b></div><span class="padd">Add to cart</span></div></article>
    <article class="pcard" style="left:51.5px;top:705.5px;width:72.5px;height:74px"><div class="pimg" style="height:47.5px;background:linear-gradient(160deg,#e9a94e,#f2ead9)" role="img" aria-label="White tote bag on orange background"><i class="heart"></i></div><div class="pinfo"><div class="prow"><span>Bag - Lorem Ipsum</span><span>€ 16.90</span></div><div class="psub">6 Different Designs Available</div><div class="stars">★★★★★<b>(12)</b></div><span class="padd">Add to cart</span></div></article>
    <article class="pcard" style="left:129.5px;top:705.5px;width:72.5px;height:74px"><div class="pimg" style="height:47.5px;background:linear-gradient(160deg,#8fd1c6,#c9a7d8)" role="img" aria-label="Striped beach towel"><i class="heart"></i></div><div class="pinfo"><div class="prow"><span>Towel - Lorem Ipsum</span><span>€ 16.90</span></div><div class="psub">6 Different Designs Available</div><div class="stars">★★★★★<b>(12)</b></div><span class="padd">Add to cart</span></div></article>
    <article class="pcard" style="left:207.5px;top:705.5px;width:72.5px;height:74px"><div class="pimg" style="height:47.5px;background:linear-gradient(160deg,#79bdb2,#2f3a3a)" role="img" aria-label="Patterned scrunchie on teal background"><i class="heart"></i></div><div class="pinfo"><div class="prow"><span>Scrunches - Lorem Ipsum</span><span>€ 16.90</span></div><div class="psub">6 Different Designs Available</div><div class="stars">★★★★★<b>(12)</b></div><span class="padd">Add to cart</span></div></article>
    <article class="pcard" style="left:286px;top:705.5px;width:72.5px;height:74px"><div class="pimg" style="height:47.5px;background:linear-gradient(160deg,#7f9ac4,#c98d73)" role="img" aria-label="Patterned bucket hat on blue background"><i class="heart"></i></div><div class="pinfo"><div class="prow"><span>Pouch - Lorem Ipsum</span><span>€ 16.90</span></div><div class="psub">6 Different Designs Available</div><div class="stars">★★★★★<b>(12)</b></div><span class="padd">Add to cart</span></div></article>

    <h2 class="section-title" style="top:791.5px">Services to Help You Shop</h2>
    <article class="svc" style="left:51.5px"><div class="svc-img" style="background:linear-gradient(160deg,#6a5a4e,#2f4a78)" role="img" aria-label="Group of people in a lively room"></div><h4>Frequently Asked Questions</h4><p>Updates on safe shopping on our store</p><span class="padd">Read More</span></article>
    <article class="svc" style="left:156px"><div class="svc-img" style="background:linear-gradient(160deg,#cdbba4,#8e7a66)" role="img" aria-label="Courier handing a parcel to a customer"></div><h4>Home Delivery Options</h4><p>Updates on safe shopping on our store</p><span class="padd">Read More</span></article>
    <article class="svc" style="left:260px"><div class="svc-img" style="background:linear-gradient(160deg,#e7e3da,#6d7f8e)" role="img" aria-label="Person paying online from a sofa"></div><h4>Online Payment Process</h4><p>Updates on safe shopping on our store</p><span class="padd">Read More</span></article>

    <footer class="abs footer">
      <div class="foot-links"><span>Terms of Services</span><span>Privacy Policy</span><span>Site Map</span></div>
      <div class="foot-follow"><span>Follow Us</span><i></i><i></i><i></i><i></i></div>
      <div class="foot-rule" style="top:20.5px"></div>
      <div class="foot-col" style="left:51.5px"><h5>About</h5><ul><li>About Us</li><li>Services</li><li>Terms of Service</li></ul></div>
      <div class="foot-col" style="left:130.5px"><h5>Categories</h5><ul><li>Bags</li><li>Jokey caps</li><li>Scrunches</li><li>Tote bags</li><li>Hat</li><li>Towel</li></ul></div>
      <div class="foot-col" style="left:208.5px"><h5>Support</h5><ul><li>Help &amp; Support</li><li>FAQ's</li><li>Contact Us</li><li>Services</li></ul></div>
      <div class="foot-col" style="left:284px"><h5>Subscribe</h5></div>
      <div class="sub-box"><span>Submit</span></div>
      <div class="apps"><h5>Apps</h5><ul><li><i></i>IOS App</li><li><i></i>Android App</li></ul></div>
      <div class="foot-rule" style="top:107px"></div>
      <p class="copyright">Copyright © 2022 Thalori - SummerWear</p>
    </footer>
  </main>

  <div class="watermark wm-1">LANDING</div>
  <div class="watermark wm-2">PAGE</div>
</div>
</body>
</html>
```